d.m.t vape cartridge .5ml 510 tread cartridge

need a logo for a new vape call “plum wedge” i need the packaging to be design and i need a logo for PLUM WEDGE, that's the name of the vape cartridge. plum wedge logo in front of box, d.m.t maybe on top and bottom, and plum wedge on both sides

i need the packaging to be design, if you search dmt on zintra you will see the same type of pics, its trippy kinda pics, neon color etc etc i want the packaging to be colorful like the pics i uploaded, and have the plum wedge logo on top above the cut out opening in front. and on the side on the box have the word plum wedge going up and down it. and on top and bottom when the box is folded i want D.M.T on it. i uploaded a cut out of the packaging

Target Market(s)

vape shops, smoke shops

Industry/Entity Type

vaping, smoking

Logo Text

the mean logo will be PLUM WEDGE i that on the front of the box and on the both sides

Logo styles of interest
Emblem Logo
Pictorial/Combination Logo
Character Logo
Font styles to use
Other font styles liked:
• any font is ok as long as it look nice

Requirements
Must have
• the word plum wedge and d.m.t
Nice to have
Should not have
• open for any ideas

```html
<!DOCTYPE html>
<html lang="en">
<head>
<meta charset="utf-8">
<title>Plum Wedge Outer Box Dieline</title>
<link rel="stylesheet" href="https://fonts.googleapis.com/css2?family=Montserrat:wght@700&family=Tinos:wght@400&display=swap">
<style>
  :root {
    --paper: #ffffff;
    --ink: #000000;
    --cut: #333333;
    --fold: #8cc870;
    --dim: #a561a5;
    --neon-magenta: #ff3fd2;
    --neon-violet: #8a3dff;
    --neon-cyan: #2ee6ff;
  }
  html, body {
    margin: 0;
    padding: 0;
    width: 1200px;
    height: 1000px;
    overflow: hidden;
    background: var(--paper);
  }
  .dieline-sheet {
    display: block;
    width: 1200px;
    height: 1000px;
  }
  .sheet-title {
    font-family: "Tinos", "Times New Roman", serif;
    font-weight: 400;
    fill: var(--ink);
    font-size: 62px;
  }
  .cut-line { fill: none; stroke: var(--cut); stroke-width: 3; }
  .fold-line { fill: none; stroke: var(--fold); stroke-width: 3; }
  .dim-line { fill: none; stroke: var(--dim); stroke-width: 2; }
  .dim-label {
    font-family: "Tinos", "Times New Roman", serif;
    font-size: 40px;
    fill: var(--dim);
  }
  .wordmark {
    font-family: "Montserrat", Arial, sans-serif;
    font-weight: 700;
    fill: var(--ink);
  }
  .flap-label {
    font-family: "Montserrat", Arial, sans-serif;
    font-weight: 700;
    font-size: 64px;
    fill: var(--ink);
  }
  .stop-magenta { stop-color: var(--neon-magenta); }
  .stop-violet { stop-color: var(--neon-violet); }
  .stop-cyan { stop-color: var(--neon-cyan); }
</style>
</head>
<body>
<svg class="dieline-sheet" viewBox="0 0 2100 1750" xmlns="http://www.w3.org/2000/svg">
  <defs>
    <linearGradient id="neon-wash" x1="0" y1="0" x2="1" y2="1">
      <stop offset="0" class="stop-magenta" stop-opacity="0.45"/>
      <stop offset="0.5" class="stop-violet" stop-opacity="0.35"/>
      <stop offset="1" class="stop-cyan" stop-opacity="0.45"/>
    </linearGradient>
  </defs>

  <!-- heading -->
  <text class="sheet-title" x="637" y="238" text-anchor="middle">Outer Box</text>
  <text class="sheet-title" x="634" y="312" text-anchor="middle">76x38x19mm</text>

  <!-- cut outline -->
  <path class="cut-line" d="M133,548 L133,402 L458,402 L458,530 L462,553 L475,532 L475,430 L602,430 L614,532 L630,553 L632,396 L962,396 L962,540 L966,553 L982,532 L992,430 L1120,430 L1120,532 L1135,549 L1227,571 L1227,1260 L1150,1260 L1140,1245 Q1130,1236 1126,1250 L1126,1327 L975,1327 L975,1250 Q975,1242 966,1242 Q958,1242 957,1250 L957,1327 L638,1327 L638,1250 Q638,1242 630,1242 Q621,1242 621,1250 L621,1327 L471,1327 L471,1250 Q471,1242 462,1242 Q454,1242 453,1250 L453,1327 L139,1327 L139,1248 L130,1233 L130,560 Z"/>

  <!-- fold lines -->
  <rect class="fold-line" x="130" y="561" width="1004" height="672"/>
  <line class="fold-line" x1="462" y1="561" x2="462" y2="1233"/>
  <line class="fold-line" x1="629" y1="561" x2="629" y2="1233"/>
  <line class="fold-line" x1="966" y1="561" x2="966" y2="1233"/>

  <!-- internal cuts -->
  <circle class="cut-line" cx="545" cy="1048" r="39"/>
  <path class="cut-line" d="M488,1233 A57,57 0 0 1 602,1233"/>
  <path class="cut-line" d="M992,1233 A58,58 0 0 1 1108,1233"/>
  <rect class="cut-line" x="757" y="738" width="80" height="318" rx="40"/>

  <!-- top flaps: D.M.T -->
  <g class="flap-dmt">
    <rect x="145" y="425" width="298" height="120" fill="url(#neon-wash)" role="img" aria-label="DMT molecule structural formula"/>
    <text class="flap-label" x="294" y="508" text-anchor="middle">D.M.T</text>
  </g>
  <g class="flap-dmt">
    <rect x="655" y="425" width="298" height="120" fill="url(#neon-wash)" role="img" aria-label="DMT molecule structural formula"/>
    <text class="flap-label" x="804" y="508" text-anchor="middle">D.M.T</text>
  </g>

  <!-- wordmarks -->
  <g class="wordmark-side-left">
    <text class="wordmark" transform="translate(338,578) rotate(90)" font-size="136" textLength="410" lengthAdjust="spacingAndGlyphs">PLUM</text>
    <text class="wordmark" transform="translate(210,585) rotate(90)" font-size="136" textLength="400" lengthAdjust="spacingAndGlyphs">WEDGE</text>
  </g>
  <g class="wordmark-front">
    <text class="wordmark" x="672" y="650" font-size="86" textLength="263" lengthAdjust="spacingAndGlyphs">PLUM</text>
    <text class="wordmark" x="670" y="725" font-size="88" textLength="270" lengthAdjust="spacingAndGlyphs">WEDGE</text>
  </g>
  <text class="wordmark" transform="translate(1012,583) rotate(90)" font-size="104" textLength="542" lengthAdjust="spacingAndGlyphs">PLUM WEDGE</text>
  <g class="wordmark-large">
    <text class="wordmark" transform="translate(1742,490) rotate(90)" font-size="254" textLength="775" lengthAdjust="spacingAndGlyphs">PLUM</text>
    <text class="wordmark" transform="translate(1500,483) rotate(90)" font-size="260" textLength="760" lengthAdjust="spacingAndGlyphs">WEDGE</text>
  </g>

  <!-- dimensions: slot -->
  <line class="dim-line" x1="718" y1="740" x2="718" y2="1055"/>
  <line class="dim-line" x1="706" y1="740" x2="762" y2="740"/>
  <line class="dim-line" x1="706" y1="1055" x2="762" y2="1055"/>
  <text class="dim-label" transform="translate(710,898) rotate(-90)" text-anchor="middle">36</text>
  <line class="dim-line" x1="758" y1="1108" x2="838" y2="1108"/>
  <line class="dim-line" x1="758" y1="1065" x2="758" y2="1120"/>
  <line class="dim-line" x1="838" y1="1065" x2="838" y2="1120"/>
  <text class="dim-label" x="795" y="1100" text-anchor="middle">9</text>

  <!-- dimensions: height -->
  <line class="dim-line" x1="1315" y1="395" x2="1315" y2="1233"/>
  <line class="dim-line" x1="1272" y1="395" x2="1326" y2="395"/>
  <line class="dim-line" x1="1272" y1="561" x2="1326" y2="561"/>
  <line class="dim-line" x1="1272" y1="1233" x2="1326" y2="1233"/>
  <text class="dim-label" transform="translate(1307,480) rotate(-90)" text-anchor="middle">18.8</text>
  <text class="dim-label" transform="translate(1307,897) rotate(-90)" text-anchor="middle">76</text>

  <!-- dimensions: widths -->
  <line class="dim-line" x1="130" y1="1412" x2="1134" y2="1412"/>
  <line class="dim-line" x1="130" y1="1368" x2="130" y2="1422"/>
  <line class="dim-line" x1="462" y1="1368" x2="462" y2="1422"/>
  <line class="dim-line" x1="629" y1="1368" x2="629" y2="1422"/>
  <line class="dim-line" x1="966" y1="1368" x2="966" y2="1422"/>
  <line class="dim-line" x1="1134" y1="1368" x2="1134" y2="1422"/>
  <text class="dim-label" x="293" y="1405" text-anchor="middle">37.5</text>
  <text class="dim-label" x="545" y="1405" text-anchor="middle">19</text>
  <text class="dim-label" x="795" y="1405" text-anchor="middle">38</text>
  <text class="dim-label" x="1048" y="1405" text-anchor="middle">19</text>
</svg>
</body>
</html>
```